Artisan Bread Company needs a business card

I need a business card design, for an artisan bread company called "Hollin's Bread".

I would like the logo on one side, and on the other, I would like it to say

Tavish Hollin
Baker
519.362.4175
hollinsbread@mailvexo.com

Not necessarily in that order- but it must have these.

Industry/Entity Type

Business

Font styles to use
Serif

Requirements
Must have
• The provided logo on the front, this on the back-
• Tavish Hollin
• Baker
• 519.362.4175
• hollinsbread@mailvexo.com

```html
<!DOCTYPE html>
<html lang="en">
<head>
<meta charset="utf-8">
<title>Hollin's Bread – Business Card</title>
<link rel="stylesheet" href="https://fonts.googleapis.com/css2?family=Open+Sans:wght@400;600&display=swap">
<style>
  :root {
    --ink: #111111;
    --paper: #ffffff;
    --muted: #555555;
    --text: #222222;
    --backdrop: #e9e6e2;
    --grain-light: #3a3836;
    --band-light: #2a2a2a;
  }
  * { box-sizing: border-box; margin: 0; padding: 0; }
  html, body {
    width: 1200px;
    height: 649px;
    overflow: hidden;
  }
  body {
    background: var(--backdrop);
    font-family: "Open Sans", Arial, sans-serif;
    position: relative;
  }
  .card {
    position: absolute;
    top: 170px;
    width: 545px;
    height: 310px;
    overflow: hidden;
    box-shadow: 0 6px 18px rgba(0,0,0,0.18);
  }

  /* Front: dark side with brand name */
  .card-front {
    left: 38px;
    background: var(--ink);
    color: var(--paper);
  }
  .card-front .decoration {
    position: absolute;
    right: 0;
    top: 0;
    width: 320px;
    height: 310px;
    background: radial-gradient(ellipse 60% 55% at 65% 42%, var(--grain-light) 0%, var(--ink) 100%);
  }
  .brand {
    position: absolute;
    display: flex;
    align-items: center;
    gap: 12px;
    white-space: nowrap;
  }
  .card-front .brand { left: 34px; top: 186px; }
  .brand-dot {
    width: 12px;
    height: 12px;
    border-radius: 50%;
    background: currentColor;
    flex: none;
  }
  .brand-name {
    font-size: 30px;
    font-weight: 400;
    letter-spacing: 0.5px;
    line-height: 1;
  }
  .card-front .website {
    position: absolute;
    left: 34px;
    top: 264px;
    font-size: 14px;
    letter-spacing: 1.4px;
  }

  /* Back: white side with contact details */
  .card-back {
    left: 617px;
    background: var(--paper);
    color: var(--ink);
  }
  .card-back .brand { left: 40px; top: 132px; gap: 10px; }
  .card-back .brand-name { font-size: 26px; }
  .contact {
    position: absolute;
    left: 297px;
    top: 105px;
  }
  .contact-name {
    font-size: 20px;
    font-weight: 600;
    line-height: 1.2;
  }
  .contact-role {
    font-size: 14px;
    color: var(--muted);
    margin-top: 2px;
    margin-bottom: 12px;
  }
  .contact-line {
    display: flex;
    align-items: center;
    gap: 8px;
    font-size: 14px;
    color: var(--text);
    line-height: 22px;
    white-space: nowrap;
  }
  .contact-line svg { width: 13px; height: 13px; fill: var(--ink); flex: none; }
  .footer-band {
    position: absolute;
    left: 0;
    bottom: 0;
    width: 545px;
    height: 40px;
    background: linear-gradient(90deg, var(--ink) 0%, var(--band-light) 100%);
  }
</style>
</head>
<body>

  <section class="card card-front" aria-label="Card front">
    <div class="decoration" role="img" aria-label="Large white wheat ear decoration"></div>
    <div class="brand">
      <span class="brand-dot"></span>
      <span class="brand-name">Hollin's Bread</span>
    </div>
    <p class="website">www.hollinsbread.com</p>
  </section>

  <section class="card card-back" aria-label="Card back">
    <div class="brand">
      <span class="brand-dot"></span>
      <span class="brand-name">Hollin's Bread</span>
    </div>

    <div class="contact">
      <p class="contact-name">Tavish Hollin</p>
      <p class="contact-role">Baker</p>
      <p class="contact-line">
        <svg viewBox="0 0 24 24" aria-hidden="true"><path d="M6.6 10.8a15.1 15.1 0 0 0 6.6 6.6l2.2-2.2a1 1 0 0 1 1-.25 11.4 11.4 0 0 0 3.6.57 1 1 0 0 1 1 1V20a1 1 0 0 1-1 1A17 17 0 0 1 3 4a1 1 0 0 1 1-1h3.5a1 1 0 0 1 1 1c0 1.25.2 2.45.57 3.57a1 1 0 0 1-.25 1z"/></svg>
        519.362.4175
      </p>
      <p class="contact-line">
        <svg viewBox="0 0 24 24" aria-hidden="true"><path d="M2 5h20v2l-10 6L2 7z"/><path d="M2 9l10 6 10-6v10H2z"/></svg>
        hollinsbread@mailvexo.com
      </p>
    </div>

    <div class="footer-band" role="img" aria-label="Dark decorative wave band along the bottom edge"></div>
  </section>

</body>
</html>
```